French version of popular website and translation

Translate existing website
Design simple copy of existing website in french

Logo stays the same
Content and pages stay the same

We just need to translate the website(s) and provide functional version of french website.

Please goto www.luvo.ca and new.luvo.ca

These 2 websites need to be copied, and 1 new french website needs to be created with existing content

We will then create a new website

www.luvo.ca/fr

There our new French website will be accessible, and our french team will be able to update it

Font styles to use
Sans Serif

Colors
cee9f5
cadf82
86cfc6
9bcb3b
aeded8
33b8a4
0dac94
00a990

Requirements
Must have
• Existing logo
• Existing photos from charities
• Existing information about our organization
Nice to have
• www.luvo.ca ( copy all pages with text and content)
• new.luvo.ca ( copy all pages with text and content)

```html
<!DOCTYPE html>
<html lang="fr">
<head>
<meta charset="utf-8">
<title>Luvo Recycling Association</title>
<link rel="stylesheet" href="https://fonts.googleapis.com/css2?family=Open+Sans:ital,wght@0,300;0,400;0,600;1,400&family=Roboto+Condensed:wght@300;400&display=swap">
<style>
:root{
  --teal:#33b8a4;
  --teal-dark:#0dac94;
  --teal-band:#1e9c8a;
  --green:#9bcb3b;
  --text:#333;
  --muted:#555;
  --hero-a:#2f3d50;
  --hero-b:#5a6b7f;
  --light:#ececec;
  --footer:#1f1f1f;
  --white:#fff;
}
*{box-sizing:border-box;margin:0;padding:0}
html,body{width:1200px;height:3209px;overflow:hidden}
body{font-family:"Open Sans",Arial,sans-serif;color:var(--text);background:var(--white);position:relative}
a{text-decoration:none;color:inherit}

/* Hero */
.hero{position:absolute;left:0;top:0;width:1200px;height:602px;background:linear-gradient(160deg,var(--hero-b) 0%,var(--hero-a) 55%,#27333f 100%)}
.brand{position:absolute;left:92px;top:44px;display:flex;align-items:center;gap:14px;color:var(--white);font-size:22px;font-weight:400}
.brand-dot{width:54px;height:54px;border:3px solid var(--white);border-radius:50%}
.main-nav{position:absolute;left:510px;top:56px;display:flex;gap:30px;color:var(--white);font-size:16px;text-transform:uppercase}
.hero-title{position:absolute;left:0;width:1200px;top:265px;text-align:center;color:var(--white);font-family:"Roboto Condensed",Arial,sans-serif;font-weight:400;font-size:58px;letter-spacing:0}
.hero-sub{position:absolute;left:0;width:1200px;top:338px;text-align:center;color:var(--white);font-size:24px;font-weight:400}
.hero-arrow{position:absolute;top:292px;width:24px;height:24px;border-radius:50%;background:#111}
.hero-arrow svg{display:block}

/* Advantages */
.section-title{position:absolute;left:0;width:1200px;text-align:center;font-size:31px;font-weight:400;text-transform:uppercase;color:#222}
.intro{position:absolute;left:150px;width:900px;text-align:center;font-size:14px;line-height:23px;color:var(--muted)}
.feature{position:absolute;width:240px;text-align:center}
.feature-icon{width:106px;height:106px;border-radius:50%;margin:0 auto;display:flex;align-items:center;justify-content:center;box-shadow:0 4px 8px rgba(0,0,0,.2)}
.feature h3{font-weight:400;font-size:22px;margin-top:32px;text-transform:uppercase}
.feature p{font-size:14px;line-height:21px;color:var(--muted);margin-top:10px;height:42px;overflow:hidden}
.feature .more{display:block;font-size:14px;margin-top:10px}

/* Reuse */
.reuse-frame{position:absolute;left:92px;top:1235px;width:395px;height:210px;background:var(--teal-dark)}
.reuse-photo{position:absolute;left:108px;top:1250px;width:415px;height:275px;background:linear-gradient(135deg,#c9b9a6,#6b7f95 60%,#3b4a5a);box-shadow:0 8px 18px rgba(0,0,0,.3)}
.reuse-title{position:absolute;left:578px;top:1250px;font-size:27px;font-weight:400;line-height:34px;text-transform:uppercase}
.reuse-text{position:absolute;left:578px;top:1326px;width:560px;height:115px;overflow:hidden;font-size:14px;line-height:23px;color:var(--muted)}
.btn-green{position:absolute;left:578px;top:1468px;width:107px;height:30px;border-radius:15px;background:var(--green);color:var(--white);font-size:13px;line-height:30px;text-align:center}

/* Highlights */
.band{position:absolute;left:0;top:1623px;width:1200px;height:267px;background:linear-gradient(180deg,#2a9d8d,var(--teal-band))}
.band-title{position:absolute;left:0;width:1200px;top:1690px;text-align:center;font-size:31px;font-weight:400;color:var(--white);text-transform:uppercase}
.highlight{position:absolute;top:1783px;width:290px}
.highlight-photo{width:290px;height:209px;box-shadow:0 6px 14px rgba(0,0,0,.25)}
.highlight p{margin-top:20px;font-size:17px;line-height:28px;text-transform:uppercase;color:#222}

/* News */
.news{position:absolute;left:0;top:2167px;width:1200px;height:398px;background:var(--light)}
.news-card{position:absolute;top:2322px;width:498px;height:170px;background:var(--white);box-shadow:0 4px 10px rgba(0,0,0,.12);display:flex}
.news-photo{width:165px;height:170px;flex:none}
.news-body{padding:12px 20px 0 24px}
.news-body h4{font-size:15px;font-weight:600;color:#222}
.news-date{font-size:13px;margin-top:6px}
.news-body p{font-size:13px;line-height:19px;color:var(--muted);margin-top:6px}
.news-body a{display:block;color:var(--teal);font-size:13px;margin-top:8px}

/* Donate */
.donate-text{position:absolute;left:157px;width:886px;top:2728px;text-align:center;font-size:17px;line-height:23px;color:#777}
.donate-link{position:absolute;left:0;width:1200px;top:2813px;text-align:center;font-size:16px;font-style:italic;color:var(--teal)}

/* Footer */
.footer{position:absolute;left:0;top:2910px;width:1200px;height:299px;background:var(--footer);color:var(--white)}
.footer h5{position:absolute;top:50px;font-size:15px;font-weight:400;text-transform:uppercase}
.quick-links{position:absolute;left:92px;top:88px;list-style:none;font-size:12px;line-height:21px;text-transform:uppercase}
.quick-links li::before{content:"» "}
.contact-list{position:absolute;left:310px;top:86px;list-style:none;font-size:12px;line-height:28px}
.contact-list li{display:flex;align-items:center;gap:12px}
.newsletter-note{position:absolute;left:605px;top:90px;width:240px;font-size:12px;line-height:17px}
.subscribe{position:absolute;left:605px;top:128px;display:flex}
.subscribe span{display:block;height:30px;line-height:30px;font-size:12px}
.subscribe .field{width:178px;background:var(--white);color:#999;padding-left:10px}
.subscribe .submit{width:82px;background:var(--green);text-align:center}
.social{position:absolute;left:970px;top:88px;display:flex;gap:12px}
.social span{width:26px;height:26px;background:var(--white);border-radius:3px}
.footer-rule{position:absolute;left:92px;top:225px;width:1016px;height:1px;background:#3a3a3a}
.copyright{position:absolute;left:0;width:1200px;top:251px;text-align:center;font-size:12px}
</style>
</head>
<body>

<header class="hero" role="img" aria-label="Photo de fond: feuillage de palmier sombre dans des tons bleu-gris">
  <div class="brand"><span class="brand-dot"></span><span>luvo.ca</span></div>
  <nav class="main-nav"><a>Sur</a><a>Médias</a><a>Emplacements</a><a>Mettre au vert</a><a>Contact</a></nav>
  <h1 class="hero-title">TOUT EST DEVENU VERT</h1>
  <p class="hero-sub">Neque porro quisquam est qui dolorem</p>
  <span class="hero-arrow" style="left:78px"><svg width="24" height="24" viewBox="0 0 24 24"><path d="M14 7l-5 5 5 5" stroke="#fff" stroke-width="2" fill="none"/></svg></span>
  <span class="hero-arrow" style="left:1100px"><svg width="24" height="24" viewBox="0 0 24 24"><path d="M10 7l5 5-5 5" stroke="#fff" stroke-width="2" fill="none"/></svg></span>
</header>

<h2 class="section-title" style="top:686px">Les avantages du choix de la LRA</h2>
<p class="intro" style="top:750px">La Luvo Recycling Association (LRA) est une organisation à but non lucratif qui réduit les déchets électroniques inutiles depuis 2004. Nous réduisons la contribution environnementale négative par le recyclage, la réutilisation et par le don de l'électronique et d'autres équipements informatiques. La LRA est un moyen efficace pour les organisations et les particuliers</p>

<div class="feature" style="left:127px;top:872px">
  <div class="feature-icon" style="background:var(--teal)"><svg width="44" height="44" viewBox="0 0 24 24"><path d="M3 10h4v11H3zM8 20V10l5-7c1.5 0 2 1 2 2l-1 4h6c1 0 2 1 1.7 2.2l-1.8 7.4c-.3.9-1 1.4-1.9 1.4z" fill="none" stroke="#fff" stroke-width="1.6"/></svg></div>
  <h3>Expérience</h3>
  <p>LRA est un chef de file en matière de recyclage et de réutilisation</p>
  <a class="more" style="color:var(--teal)">Lire la suite -&gt;</a>
</div>
<div class="feature" style="left:455px;top:872px">
  <div class="feature-icon" style="background:var(--green)"><svg width="40" height="40" viewBox="0 0 24 24"><rect x="5" y="11" width="14" height="10" rx="1" fill="#fff"/><path d="M8 11V8a4 4 0 018 0v3" fill="none" stroke="#fff" stroke-width="2"/></svg></div>
  <h3>Sécurité</h3>
  <p>A chaque étape du processus de récupération - du ramassage à</p>
  <a class="more" style="color:var(--green)">Lire la suite -&gt;</a>
</div>
<div class="feature" style="left:785px;top:872px">
  <div class="feature-icon" style="background:var(--teal)"><svg width="42" height="42" viewBox="0 0 24 24"><circle cx="9" cy="13" r="4.5" fill="none" stroke="#fff" stroke-width="2.5" stroke-dasharray="2.2 1.3"/><circle cx="9" cy="13" r="1.6" fill="#fff"/><circle cx="17" cy="6" r="3" fill="none" stroke="#fff" stroke-width="2" stroke-dasharray="1.6 1"/></svg></div>
  <h3>Services complets</h3>
  <p>Nous avons une gamme de services pour couvrir vos besoins en</p>
  <a class="more" style="color:var(--teal)">Lire la suite -&gt;</a>
</div>

<div class="reuse-frame"></div>
<div class="reuse-photo" role="img" aria-label="Photo de deux bénévoles tenant un ordinateur portable dans un bureau"></div>
<h2 class="reuse-title">Réutilisation informatique<br>et électronique</h2>
<p class="reuse-text">La Luvo Recycling Association (LRA) est une organisation à but non lucratif qui réduit les déchets électroniques inutiles depuis 2004. Nous réduisons la contribution environnementale négative par le recyclage, la réutilisation et par le don de l'électronique et d'autres équipements informatiques. La LRA est un moyen efficace pour les organisations et les particuliers de faire face à leur ancien équipement informatique dans un environnement où les services</p>
<a class="btn-green">Lire la suite</a>

<div class="band" role="img" aria-label="Bande sarcelle avec feuillage en transparence"></div>
<h2 class="band-title">Dernières informatiques et recyclage de l'électronique</h2>
<div class="highlight" style="left:108px"><div class="highlight-photo" role="img" aria-label="Photo de trois bénévoles lors d'un événement" style="background:linear-gradient(135deg,#a9c8c2,#4c4a4e 60%,#2b2b2f)"></div><p>Cliquez ici<br>pour 2017 faits saillants</p></div>
<div class="highlight" style="left:457px"><div class="highlight-photo" role="img" aria-label="Photo de deux enfants avec une tablette" style="background:linear-gradient(135deg,#6e8fb0,#b49c8a 55%,#3a4e6a)"></div><p>Cliquez ici<br>pour 2016 faits saillants</p></div>
<div class="highlight" style="left:800px"><div class="highlight-photo" role="img" aria-label="Photo d'une équipe devant un camion de collecte" style="background:linear-gradient(135deg,#e5e2dc,#8a8d8e 55%,#7a2a2a)"></div><p>Cliquez ici<br>pour 2015 faits saillants</p></div>

<section class="news" role="img" aria-label="Fond gris clair avec photo d'entrepôt estompée"></section>
<h2 class="section-title" style="top:2235px">Nouvelles récentes</h2>
<article class="news-card" style="left:92px">
  <div class="news-photo" role="img" aria-label="Photo de deux personnes lors d'un don" style="background:linear-gradient(135deg,#7fb0a8,#c23b3b 60%,#2f3a3a)"></div>
  <div class="news-body"><h4>La LRA aide un parent nourricier</h4><div class="news-date">09-07-2017</div><p>Lorem Ipsum has been the industry's standard dummy text ever since the 1500s, when an unknown printer took a galley of type</p><a>Lire la suite &gt;&gt;</a></div>
</article>
<article class="news-card" style="left:614px">
  <div class="news-photo" role="img" aria-label="Photo d'un ordinateur portable sur une table" style="background:linear-gradient(135deg,#5c4a3a,#2a2622 55%,#1c1a18)"></div>
  <div class="news-body"><h4>LRA Partenariat avec Centre Belvarin</h4><div class="news-date">09-07-2017</div><p>Lorem Ipsum has been the industry's standard dummy text ever since the 1500s, when an unknown printer took a galley of type</p><a>Lire la suite &gt;&gt;</a></div>
</article>

<h2 class="section-title" style="top:2672px">Êtes-vous prêt à combler les autres? Donnez aujourd'hui</h2>
<p class="donate-text">Les dons de matériel indésirable aident à garder les déchets électroniques inutiles hors des sites d'enfouissement. Avec nos programmes de réutilisation, vos dons sont revitalisés et une nouvelle maison est offerte. Si l'électronique ne peut absolument pas être réutilisée, nous la recyclerons.</p>
<a class="donate-link">RÉSERVER UNE PICKUP</a>

<footer class="footer">
  <h5 style="left:92px">Liens rapides</h5>
  <ul class="quick-links"><li>Sur</li><li>Médias</li><li>Emplacements</li><li>Mettre au vert</li></ul>
  <h5 style="left:310px">Contactez nous</h5>
  <ul class="contact-list">
    <li><svg width="10" height="13" viewBox="0 0 10 13"><path d="M5 0a4.5 4.5 0 00-4.5 4.5C.5 8 5 13 5 13s4.5-5 4.5-8.5A4.5 4.5 0 005 0z" fill="#fff"/><circle cx="5" cy="4.5" r="1.6" fill="#1f1f1f"/></svg>Luvo Recycling Association</li>
    <li><svg width="11" height="11" viewBox="0 0 24 24"><path d="M6.6 10.8a15 15 0 006.6 6.6l2.2-2.2c.3-.3.7-.4 1-.2 1.1.4 2.3.6 3.6.6.6 0 1 .4 1 1V20c0 .6-.4 1-1 1A17 17 0 013 4c0-.6.4-1 1-1h3.5c.6 0 1 .4 1 1 0 1.3.2 2.5.6 3.6.1.3 0 .7-.2 1z" fill="#fff"/></svg>1.877.555.0142</li>
    <li><svg width="12" height="9" viewBox="0 0 12 9"><rect width="12" height="9" fill="#fff"/><path d="M0 0l6 5 6-5" stroke="#1f1f1f" fill="none"/></svg>info@luvo.ca</li>
  </ul>
  <h5 style="left:605px">Joignez-vous à notre liste d'envoi</h5>
  <p class="newsletter-note">Votre information sur nous correspondrait ici gentiment.</p>
  <div class="subscribe"><span class="field">Adresse e-mail</span><span class="submit">Soumettre</span></div>
  <h5 style="left:970px">Suivez-nous</h5>
  <div class="social"><span></span><span></span><span></span><span></span></div>
  <div class="footer-rule"></div>
  <p class="copyright">Copyright © 2017 All Rights Reserved</p>
</footer>

</body>
</html>
```